Business Card Design Project

I have attached the logo and the colour pallete for the branding for the company.

Creative designs for business cards are needed.

The Company is modern corporate.

Industry/Entity Type

Business

```html
<!DOCTYPE html>
<html lang="en">
<head>
<meta charset="utf-8">
<title>routely business cards</title>
<link href="https://fonts.googleapis.com/css2?family=Montserrat:wght@400;600;700&display=swap" rel="stylesheet">
<style>
  :root {
    --backdrop: #8a8a8a;
    --purple-deep: #3c1240;
    --purple: #5e1f63;
    --purple-brand: #6a2470;
    --orange: #e8722a;
    --grey-drop: #c9c9c9;
    --paper: #f6f6f4;
    --ink-soft: #8c8c8c;
    --ink-label: #6e6e6e;
  }
  * { margin: 0; padding: 0; box-sizing: border-box; }
  html, body {
    width: 1200px;
    height: 1000px;
    overflow: hidden;
  }
  body {
    background: var(--backdrop);
    font-family: "Montserrat", sans-serif;
    position: relative;
  }
  .card {
    position: absolute;
    left: 250px;
    width: 700px;
    height: 400px;
    border-radius: 4px;
    box-shadow: 0 10px 30px rgba(0,0,0,0.3);
    overflow: hidden;
  }
  .card-front {
    top: 60px;
    background: radial-gradient(ellipse at 65% 40%, var(--purple) 0%, var(--purple-deep) 90%);
    display: flex;
    align-items: center;
    justify-content: center;
  }
  .wordmark {
    font-weight: 700;
    letter-spacing: -1px;
    line-height: 1;
  }
  .card-front .wordmark {
    color: #ffffff;
    font-size: 84px;
  }
  .card-back {
    top: 540px;
    background: var(--paper);
  }
  .drops-decoration {
    position: absolute;
    left: 0;
    top: 0;
    width: 240px;
    height: 120px;
    background: linear-gradient(100deg, var(--orange) 0%, var(--purple-brand) 35%, var(--grey-drop) 70%, var(--paper) 100%);
    opacity: 0.85;
    border-bottom-right-radius: 60px;
  }
  .brand-block {
    position: absolute;
    left: 50px;
    top: 220px;
    display: flex;
    align-items: center;
  }
  .card-back .wordmark {
    color: var(--purple-brand);
    font-size: 68px;
  }
  .divider {
    width: 1px;
    height: 90px;
    background: #b5b5b5;
    margin: 0 20px 0 32px;
  }
  .contact-list {
    list-style: none;
    font-size: 17px;
    color: var(--ink-soft);
    line-height: 1.45;
  }
  .contact-list b {
    color: var(--ink-label);
    font-weight: 700;
    margin-right: 4px;
  }
</style>
</head>
<body>
  <section class="card card-front">
    <span class="wordmark">routely</span>
  </section>

  <section class="card card-back">
    <div class="drops-decoration" role="img" aria-label="Decorative cluster of purple, orange and grey drop shapes"></div>
    <div class="brand-block">
      <span class="wordmark">routely</span>
      <span class="divider"></span>
      <ul class="contact-list">
        <li><b>e.</b>info@routely.com</li>
        <li><b>t.</b>(555) 010-2040</li>
        <li><b>w.</b>www.routely.com</li>
      </ul>
    </div>
  </section>
</body>
</html>
```